Photo Storage Service - Web Application

This is web design for a simple photo storage service.
There is a web page and on the left side is a list of folders and on the right side there are photo thumbnails. By pressing a photo thumbnail, they will see the full size (it's just a link to a different page).
This project is limited only to ONE page, which is the page with the folders list and the thumbnails. However it contains some features that I will try to list here:
- Name of the service: Tavo Vault
- Location of account: http://username.tavo.example
- Folder list: Show all folders belonging to the user. Because you have to be able to drag photos to a folder, they have to be visible and cannot be hidden behind a menu item etc.
- Thumbnails with photos (in the future also videos)
- Adjusted view with smaller thumbnails and less space for folder list (so it is possible to view a larger quantity of thumbnails)- Select multiple thumbnails with rectangle- Show that a thumbnail is selected (maybe bold border?)
- Simple mobile view, but no emphasis on the mobile view in this design project.
- Drag one or more selected photos to a folder
- Delete one or more selected photos
- Drag a folder to another folder
- Rename folder
- Delete folder
- Create folder
- Show progress when deleting/moving (because it calls for every photo, so if there are 100 photos, it will delete 1 by 1 and it will take about 10 seconds - you could show progress bar or equivalent)
Background information: This is for a photo storage service NOT intended for sharing photos, but intended to indefinitely store photos and for yourself to browse your own photos.
It is a design requirement that it loads extremely fast. So we need to limit as much as possible extra graphics that cannot be done by CSS and other external libraries.
(I know this is ONLY design and nothing to do with CSS or libraries, but I can assess from the design if it might be heavy to load when implemented)
I have attached a crude screenshot of the current design, just for your understanding. It should not match this design and you are not in any way supposed to FIT your design into this same style or structure.
Target Market(s)
Consumers
Number of Pages Required
1 page
Font styles to use
Look and feel
Each slider illustrates characteristics of the customer's brand and the style your logo design should communicate.

```html
<!DOCTYPE html>
<html lang="en">
<head>
<meta charset="utf-8">
<title>Tavo Vault</title>
<link href="https://fonts.googleapis.com/css2?family=Montserrat:wght@400;500;600&display=swap" rel="stylesheet">
<style>
  :root {
    --green: #1bb68c;
    --ink: #1f2024;
    --text: #2b2d33;
    --muted: #707378;
    --faint: #c9ccd0;
    --topbar: #eceef1;
    --sidebar: #f3f4f6;
    --pill-hover: #d2d4d8;
    --select-border: #2a9d86;
    --white: #ffffff;
  }
  * { box-sizing: border-box; margin: 0; padding: 0; }
  html, body { width: 1200px; height: 750px; overflow: hidden; background: var(--white); }
  body { position: relative; font-family: "Montserrat", sans-serif; color: var(--text); }

  .topbar { position: absolute; left: 0; top: 0; width: 1200px; height: 51px; background: var(--topbar); }
  .sidebar { position: absolute; left: 0; top: 0; width: 266px; height: 750px; background: linear-gradient(180deg, #eef0f2 0%, #f6f7f8 100%); }
  .brand { position: absolute; left: 49px; top: 13px; font-size: 18px; font-weight: 400; color: var(--text); letter-spacing: .2px; }

  .account { position: absolute; left: 950px; top: 9px; height: 32px; display: flex; align-items: center; }
  .avatar { width: 32px; height: 32px; border-radius: 50%; background: linear-gradient(135deg, #6f5a4c, #c9b7a6); }
  .account-name { margin-left: 5px; font-size: 11px; color: var(--text); }
  .kebab { position: absolute; left: 1075px; top: 18px; }
  .account-menu { position: absolute; left: 986px; top: 36px; width: 92px; box-shadow: 0 2px 6px rgba(0,0,0,.12); background: var(--white); font-size: 8px; text-align: center; }
  .account-menu .item { height: 28px; line-height: 28px; color: var(--muted); }
  .account-menu .item.signout { height: 29px; line-height: 29px; background: var(--green); color: var(--white); font-weight: 500; }

  .create-folder { position: absolute; left: 48px; top: 77px; width: 115px; height: 29px; border-radius: 15px; background: var(--green); color: var(--white); font-size: 12.5px; display: flex; align-items: center; justify-content: center; gap: 6px; box-shadow: 0 2px 5px rgba(27,182,140,.3); }

  .folder { position: absolute; left: 48px; width: 197px; height: 30px; line-height: 30px; padding-left: 16px; font-size: 10.5px; color: var(--muted); border-radius: 15px; }
  .folder.active { background: var(--ink); color: var(--white); }
  .folder.hover { background: var(--pill-hover); color: var(--text); }
  .folder .dots { position: absolute; right: 16px; top: 8px; }
  .folder-menu { position: absolute; left: 132px; top: 154px; width: 98px; background: var(--white); box-shadow: 0 2px 6px rgba(0,0,0,.12); font-size: 8.5px; }
  .folder-menu .item { height: 28px; line-height: 28px; padding-left: 14px; color: var(--text); }
  .folder-menu .item + .item { color: var(--muted); border-top: 1px solid #eee; padding-left: 18px; }

  .toolbar-action { position: absolute; top: 81px; display: flex; align-items: center; gap: 6px; font-size: 8.5px; color: var(--muted); }

  .thumb { position: absolute; width: 144px; height: 138px; }
  .thumb.selected { outline: 1px solid var(--select-border); }
  .play { position: absolute; left: 61px; top: 58px; }

  .selection { position: absolute; left: 318px; top: 114px; width: 443px; height: 316px; background: rgba(130,130,130,.55); border: 1.5px dashed #444; }
  .pointer { position: absolute; left: 759px; top: 428px; }

  .upload { position: absolute; left: 285px; top: 454px; width: 305px; height: 203px; border: 1px dashed var(--faint); }
  .upload-icon { position: absolute; left: 123px; top: 39px; }
  .upload-button { position: absolute; left: 78px; top: 101px; width: 149px; height: 31px; border-radius: 16px; background: var(--green); color: var(--white); font-size: 11px; display: flex; align-items: center; justify-content: center; }
  .upload-hint { position: absolute; left: 0; top: 146px; width: 100%; text-align: center; font-size: 10px; color: var(--faint); }

  .submit { position: absolute; left: 386px; top: 681px; width: 104px; height: 31px; border-radius: 16px; background: var(--ink); color: var(--white); font-size: 12px; display: flex; align-items: center; justify-content: center; }
</style>
</head>
<body>
  <div class="topbar"></div>
  <aside class="sidebar"></aside>
  <div class="brand">Tavo Vault</div>

  <div class="account">
    <div class="avatar" role="img" aria-label="User avatar photo"></div>
    <span class="account-name">Leon Harwick</span>
  </div>
  <svg class="kebab" width="4" height="14" viewBox="0 0 4 14"><circle cx="2" cy="2" r="1.4" fill="#333"/><circle cx="2" cy="7" r="1.4" fill="#333"/><circle cx="2" cy="12" r="1.4" fill="#333"/></svg>
  <div class="account-menu">
    <div class="item">Profile</div>
    <div class="item signout">Signout</div>
  </div>

  <div class="create-folder"><span style="font-size:15px;line-height:1">+</span>Create Folder</div>

  <div class="folder active" style="top:130px">Inbox
    <svg class="dots" width="4" height="14" viewBox="0 0 4 14"><circle cx="2" cy="2" r="1.3" fill="#fff"/><circle cx="2" cy="7" r="1.3" fill="#fff"/><circle cx="2" cy="12" r="1.3" fill="#fff"/></svg>
  </div>
  <div class="folder" style="top:160px">80,s party</div>
  <div class="folder" style="top:191px">A day in Oslo</div>
  <div class="folder" style="top:223px">A Tour of Svendborg</div>
  <div class="folder hover" style="top:254px">Alicante 2017
    <svg class="dots" width="4" height="14" viewBox="0 0 4 14"><circle cx="2" cy="2" r="1.3" fill="#fff"/><circle cx="2" cy="7" r="1.3" fill="#fff"/><circle cx="2" cy="12" r="1.3" fill="#fff"/></svg>
  </div>
  <div class="folder" style="top:285px">Bandardan</div>
  <div class="folder" style="top:316px">Brazil</div>
  <div class="folder" style="top:347px">Random</div>
  <div class="folder" style="top:379px">Thailand 1</div>
  <div class="folder" style="top:410px">Thailand 2</div>
  <div class="folder" style="top:441px">Usa</div>
  <div class="folder" style="top:472px">Thumbnails</div>
  <div class="folder" style="top:503px">Videos/thumbnails</div>

  <div class="folder-menu">
    <div class="item">Rename Folder</div>
    <div class="item">Delete Folder</div>
  </div>

  <div class="toolbar-action" style="left:286px">
    <svg width="15" height="18" viewBox="0 0 15 18" fill="none" stroke="#1bb68c" stroke-width="1.2"><path d="M1 3.5h13M5 3.5V1.5h5v2M2.5 3.5l1 13.5h8l1-13.5M6 6v9M9 6v9"/></svg>
    Delete Select Files
  </div>
  <div class="toolbar-action" style="left:432px">
    <svg width="18" height="18" viewBox="0 0 18 18" fill="none" stroke="#1bb68c" stroke-width="1.2"><rect x="1" y="1" width="10" height="10" stroke-dasharray="2 1.5"/><rect x="6" y="6" width="11" height="11"/><path d="M8 8l6 6M14 10v4h-4"/></svg>
    Drag files to the destined folder
  </div>

  <div class="thumb selected" style="left:285px;top:128px;background:linear-gradient(135deg,#8a5a36,#c98a5b 50%,#a47c6a)" role="img" aria-label="Video thumbnail: child holding a carved pumpkin">
    <svg class="play" width="22" height="22" viewBox="0 0 22 22"><circle cx="11" cy="11" r="10" fill="rgba(255,255,255,.25)" stroke="#fff" stroke-width="1.2"/><path d="M8.5 6.5l7 4.5-7 4.5z" fill="#fff"/></svg>
  </div>
  <div class="thumb selected" style="left:447px;top:128px;background:linear-gradient(135deg,#4f4a2c,#6e6438 50%,#3e3a25)" role="img" aria-label="Photo: woman lying in grass"></div>
  <div class="thumb selected" style="left:610px;top:128px;background:linear-gradient(135deg,#6b7068,#4a4f52 60%,#3a3d44)" role="img" aria-label="Photo: couple embracing outdoors"></div>
  <div class="thumb" style="left:772px;top:128px;background:linear-gradient(180deg,#f2e4cc,#d9b48b 60%,#b89477)" role="img" aria-label="Photo: mother and child on a sunset beach"></div>
  <div class="thumb" style="left:934px;top:128px;background:linear-gradient(135deg,#9d8e85,#5c5450 55%,#2e2a29)" role="img" aria-label="Photo: hands holding a camera lens"></div>

  <div class="thumb selected" style="left:285px;top:285px;background:linear-gradient(135deg,#b9a089,#8a6d52 50%,#5d4a3a)" role="img" aria-label="Photo: woman in sunglasses in a field"></div>
  <div class="thumb selected" style="left:447px;top:285px;background:linear-gradient(180deg,#6f7e99,#5a6a84 45%,#8a4a2e 60%,#3e6e7e)" role="img" aria-label="Photo: rusted shipwreck by the sea"></div>
  <div class="thumb selected" style="left:610px;top:285px;background:linear-gradient(180deg,#9a9a96,#7b7c78 60%,#5d5e5b)" role="img" aria-label="Photo: friends sitting on stone steps"></div>
  <div class="thumb" style="left:772px;top:285px;background:linear-gradient(180deg,#7d7f8c,#d9a27a 55%,#ece6e2)" role="img" aria-label="Video thumbnail: dancers at sunset">
    <svg class="play" width="22" height="22" viewBox="0 0 22 22"><circle cx="11" cy="11" r="10" fill="rgba(255,255,255,.25)" stroke="#fff" stroke-width="1.2"/><path d="M8.5 6.5l7 4.5-7 4.5z" fill="#fff"/></svg>
  </div>
  <div class="thumb" style="left:934px;top:285px;background:linear-gradient(135deg,#2f3a22,#c9352c 55%,#e2482e)" role="img" aria-label="Photo: child in a witch costume"></div>

  <div class="selection"></div>
  <svg class="pointer" width="10" height="15" viewBox="0 0 10 15"><path d="M1 1v12l3-3 2 4.5 1.8-.8-2-4.4H9.5z" fill="#111" stroke="#fff" stroke-width=".8"/></svg>

  <div class="upload">
    <svg class="upload-icon" width="60" height="46" viewBox="0 0 60 46"><path d="M14 44a13 13 0 0 1-2-25.8A17 17 0 0 1 44 12a12 12 0 0 1 4 23.5V44z" fill="#c7c9cc"/><path d="M30 14l-11 12h7v14h8V26h7z" fill="#fff"/></svg>
    <div class="upload-button">Choose files to upload</div>
    <div class="upload-hint">Drag and drop files here to upload</div>
  </div>

  <div class="submit">Submit</div>
</body>
</html>
```